KRWM new business card design

We need a business card design for our established business which is Australia wide however based in Melbourne. We are a young team of Financial Planners who specialize in Insurance and Basic super advice for people like us.

We are people who help our clients get things done in a timely and cost effective manner whilst having a good time and a laugh along the way.

We would like this to have a consistent feel with our new e-brochure which i have attached from a color and font perspective.

Industry/Entity Type

Business

Requirements
Must have
• We do not need specific address details rather just the states we are in:

VIC/NSW/QLD/TAS
Nice to have
• Curved edge to mate the brochure

```html
<!DOCTYPE html>
<html lang="en">
<head>
<meta charset="utf-8">
<title>KRWM Business Card</title>
<link rel="stylesheet" href="https://fonts.googleapis.com/css2?family=Arimo:wght@400;700&display=swap">
<style>
  :root {
    --page-bg: #e6e7e8;
    --brand-green: #6cbd45;
    --brand-green-deep: #13a24a;
    --card-white: #ffffff;
    --card-charcoal: #343434;
    --ink: #3a3a3a;
    --ink-soft: #6b6b6b;
    --ink-light: #ffffff;
    --ink-light-soft: #bdbdbd;
  }
  * { box-sizing: border-box; margin: 0; padding: 0; }
  html, body { width: 1200px; height: 800px; overflow: hidden; }
  body {
    background: var(--page-bg);
    font-family: "Arimo", Arial, sans-serif;
    display: flex;
    align-items: center;
    justify-content: center;
    gap: 40px;
  }
  .card {
    position: relative;
    width: 560px;
    height: 320px;
    overflow: hidden;
    box-shadow: 0 10px 30px rgba(0,0,0,0.18);
  }

  /* Front */
  .card-front { background: var(--brand-green); }
  .front-panel {
    position: absolute;
    left: 0; bottom: 0;
    width: 528px;
    height: 276px;
    background: var(--card-white);
    border-top-left-radius: 70px;
  }
  .brand {
    position: absolute;
    display: flex;
    align-items: center;
    gap: 12px;
  }
  .brand-mark {
    width: 34px; height: 34px;
    background: var(--brand-green);
    border-radius: 6px;
  }
  .brand-name {
    font-weight: 700;
    font-size: 46px;
    line-height: 1;
    letter-spacing: 1px;
    color: var(--brand-green-deep);
  }
  .front-panel .brand { left: 48px; top: 52px; }

  .states {
    position: absolute;
    font-weight: 700;
    font-size: 13px;
    letter-spacing: 2px;
  }
  .front-panel .states { left: 48px; top: 110px; color: var(--ink-soft); }

  .person { position: absolute; left: 290px; top: 122px; }
  .person-name {
    font-weight: 700;
    font-size: 22px;
    color: var(--brand-green);
  }
  .person-role {
    font-size: 18px;
    color: var(--ink);
    margin-top: 2px;
  }
  .contact-list {
    position: absolute;
    left: 290px; top: 192px;
    list-style: none;
  }
  .contact-item {
    display: flex;
    align-items: center;
    gap: 8px;
    font-size: 15px;
    color: var(--ink);
    height: 22px;
    white-space: nowrap;
  }
  .contact-icon { width: 15px; height: 15px; flex: none; }

  /* Back */
  .card-back { background: var(--card-charcoal); }
  .card-back .brand { left: 60px; top: 136px; }
  .back-web {
    position: absolute;
    left: 320px; top: 148px;
    font-size: 17px;
    color: var(--ink-light);
    white-space: nowrap;
  }
  .card-back .states { left: 320px; top: 176px; color: var(--ink-light-soft); }
</style>
</head>
<body>
  <section class="card card-front" aria-label="Business card front">
    <div class="front-panel">
      <div class="brand">
        <span class="brand-mark"></span>
        <span class="brand-name">KRWM</span>
      </div>
      <p class="states">VIC / NSW / QLD / TAS</p>
      <div class="person">
        <p class="person-name">Harlow</p>
        <p class="person-role">Manager</p>
      </div>
      <ul class="contact-list">
        <li class="contact-item">
          <svg class="contact-icon" viewBox="0 0 16 16" aria-hidden="true">
            <rect width="16" height="16" rx="3" fill="#6cbd45"/>
            <path d="M4.5 3.5 L6.5 3.5 L7.3 6 L6.1 7 Q7.2 9.3 9 10 L10 8.8 L12.5 9.6 L12.5 11.6 Q7 12.5 4.5 3.5 Z" fill="#fff"/>
          </svg>
          123.555.0147
        </li>
        <li class="contact-item">
          <svg class="contact-icon" viewBox="0 0 16 16" aria-hidden="true">
            <rect x="0.75" y="0.75" width="14.5" height="14.5" rx="3" fill="none" stroke="#3a3a3a" stroke-width="1.5"/>
            <path d="M3.5 5 L8 8.5 L12.5 5" fill="none" stroke="#3a3a3a" stroke-width="1.3"/>
          </svg>
          hello@krwmplanning.com.au
        </li>
        <li class="contact-item">
          <svg class="contact-icon" viewBox="0 0 16 16" aria-hidden="true">
            <rect width="16" height="16" rx="3" fill="#6cbd45"/>
            <circle cx="8" cy="8" r="4.5" fill="none" stroke="#fff" stroke-width="1.3"/>
            <path d="M3.5 8 H12.5 M8 3.5 Q5.5 8 8 12.5 M8 3.5 Q10.5 8 8 12.5" fill="none" stroke="#fff" stroke-width="1"/>
          </svg>
          www.krwmplanning.com.au
        </li>
      </ul>
    </div>
  </section>

  <section class="card card-back" aria-label="Business card back">
    <div class="brand">
      <span class="brand-mark"></span>
      <span class="brand-name">KRWM</span>
    </div>
    <p class="back-web">www.krwmplanning.com.au</p>
    <p class="states">VIC / NSW / QLD / TAS</p>
  </section>
</body>
</html>
```